Business Card Revision

Need to redesign my business cards for a new professional look. We are a courier company. You can go to www.qvrunners.com to see what we do. The trucks have an old company name (Sprout) on them but that is the company we are just now
changing the name.

Target Market(s)

Potential clients. We service the automotive, plumbing, printing, air freight industries as well as many others.

Industry/Entity Type

Business

Contact Information for Business Card

QVmotion
20864 Lark Fenmore Parkway
Larkhaven, Oh 45873

Thomas R. Wendall
President

tom@qvrunners.com

Main: (513) 555-0147

```html
<!DOCTYPE html>
<html lang="en">
<head>
<meta charset="utf-8">
<title>QV Runners Business Card</title>
<link href="https://fonts.googleapis.com/css2?family=Source+Sans+3:wght@400;600;700&display=swap" rel="stylesheet">
<style>
  :root {
    --page-bg: #e6e7e9;
    --brand-blue: #1b6fb5;
    --brand-blue-light: #3b93d3;
    --brand-blue-dark: #135a98;
    --brand-green: #3aac4a;
    --card-white: #f7f7f7;
    --card-grey: #dedfe1;
    --ink: #444a50;
    --white: #ffffff;
  }
  * { margin: 0; padding: 0; box-sizing: border-box; }
  html, body {
    width: 1200px; height: 1200px; overflow: hidden;
    background: var(--page-bg);
    font-family: "Source Sans 3", "Myriad Pro", Arial, sans-serif;
  }
  .canvas { position: relative; width: 1200px; height: 1200px; }
  .card {
    position: absolute; left: 180px; width: 840px; height: 480px;
    overflow: hidden; box-shadow: 0 10px 28px rgba(0,0,0,.18);
  }
  .card-front {
    top: 90px;
    background: linear-gradient(160deg, var(--brand-blue-dark) 0%, var(--brand-blue-light) 50%, var(--brand-blue) 100%);
  }
  .front-wordmark {
    position: absolute; left: 0; right: 0; top: 196px; text-align: center;
    color: var(--white); font-weight: 700; font-size: 52px; letter-spacing: 3px;
  }
  .front-url {
    position: absolute; left: 0; right: 0; bottom: 40px; text-align: center;
    color: var(--white); font-size: 21px; letter-spacing: 2px;
  }
  .card-back {
    top: 630px;
    background: linear-gradient(135deg, var(--card-grey) 0%, var(--card-white) 45%, var(--card-grey) 100%);
  }
  .back-art { position: absolute; inset: 0; }
  .back-wordmark {
    position: absolute; left: 30px; width: 300px; top: 190px; text-align: center;
    color: var(--brand-blue); font-weight: 700; font-size: 54px; line-height: 1; letter-spacing: 2px;
  }
  .divider {
    position: absolute; left: 355px; top: 40px; width: 2px; height: 170px;
    background: var(--brand-green);
  }
  .contact { position: absolute; left: 385px; top: 58px; }
  .contact-name { color: var(--brand-blue); font-size: 32px; font-weight: 400; line-height: 1.1; }
  .contact-title { color: var(--ink); font-size: 19px; margin-top: 2px; }
  .contact-list { list-style: none; margin-top: 14px; }
  .contact-item {
    display: flex; align-items: center; gap: 10px;
    color: var(--ink); font-size: 23px; line-height: 29px; padding-left: 8px;
  }
  .contact-icon { width: 18px; height: 18px; flex: none; }
  .address-line {
    position: absolute; left: 100px; bottom: 22px;
    color: var(--white); font-size: 21px;
  }
  .address-line strong { font-weight: 700; }
</style>
</head>
<body>
<main class="canvas">
  <section class="card card-front" aria-label="Business card front">
    <div class="front-wordmark">QV RUNNERS</div>
    <div class="front-url">www.qvrunners.com</div>
  </section>

  <section class="card card-back" aria-label="Business card back">
    <svg class="back-art" width="840" height="480" viewBox="0 0 840 480">
      <path d="M0,400 C260,385 560,355 840,280 L840,480 L0,480 Z" fill="var(--brand-blue)"/>
      <path d="M0,384 C260,369 560,338 840,262" fill="none" stroke="var(--brand-green)" stroke-width="5"/>
    </svg>
    <div class="back-wordmark">QV<br>RUNNERS</div>
    <div class="divider"></div>
    <div class="contact">
      <div class="contact-name">Thomas R. Wendall</div>
      <div class="contact-title">President</div>
      <ul class="contact-list">
        <li class="contact-item">
          <svg class="contact-icon" viewBox="0 0 18 18"><path d="M2 7c0-3 3-4 7-4s7 1 7 4l-3 1-1-2H6L5 8z M4 9h10l1 6H3z" fill="var(--brand-green)"/></svg>
          (555) 555-0147
        </li>
        <li class="contact-item">
          <svg class="contact-icon" viewBox="0 0 18 18"><rect x="1" y="4" width="16" height="11" fill="var(--brand-green)"/><path d="M1 4l8 6 8-6" fill="none" stroke="#fff" stroke-width="1.5"/></svg>
          tom@qvrunners.com
        </li>
        <li class="contact-item">
          <svg class="contact-icon" viewBox="0 0 18 18"><circle cx="9" cy="9" r="8" fill="var(--brand-green)"/><path d="M1 9h16M9 1c-4 4-4 12 0 16M9 1c4 4 4 12 0 16" fill="none" stroke="#fff" stroke-width="1.2"/></svg>
          www.qvrunners.com
        </li>
      </ul>
    </div>
    <div class="address-line"><strong>QVmotion</strong> | 20864 Lark Fenmore Parkway, Larkhaven, Vt 45873</div>
  </section>
</main>
</body>
</html>
```